Flyer for Encounter G.L.O. - Hour of Glory!

We are producing a monthly Hour of Glory that supports local Christian Contemporary artists and raises money for charities. We are looking for a flyer design for our flyers, posters, and postcards (some mailed and some handed out). We want to create a modern and impressive flyer that will capture audiences.

Event details -
Tag: experience the night. praise the night.
A Hour of Glory you will not want to miss
Let's worship! Live band covering your favorite popular contemporary Christian music! All ages welcome!
Date: Wednesday, May 27th, 2015
7:00 pm to 8:15 pm
Location: The Harborview Chapel
2715 W Maple Crest Rd; Fort Lauderdale, FL 33918

Event is FREE!! Please bring a donation of gently used clothing items or new toiletry item.
Benefit for: The Open Hands Mission

This month's debut artist: Talia Verhoeven - local Christian Singer/Songwriter.

for more details, visit: www.encounterpraiseGLO.example
brought to you by: Delphine Marsh Music
___
Please see our website for style of what we are looking for. Also attached is a template design that I like and would love to see if we can do something like this.

Target Market(s)

all ages - young, older, modern, contemporary - youth

Industry/Entity Type

Artists

Colors
ec1f27
6b449b
ffffff

Requirements
Must have
• Cool design, bring a new "vibe" to Christian music -
• Black design
• worship photos like in the attached template ideas.

```html
<!DOCTYPE html>
<html lang="en">
<head>
<meta charset="utf-8">
<title>Encounter G.L.O. - Hour of Glory</title>
<link rel="stylesheet" href="https://fonts.googleapis.com/css2?family=Michroma&family=Oswald:wght@600;700&family=Rubik+Dirt&display=swap">
<style>
  :root {
    --ink: #0b0710;
    --plum: #6b2a6e;
    --lilac: #c79ad6;
    --white: #ffffff;
    --gold: #f5c21b;
    --cream-yellow: #f4e27a;
    --sky: #a8dcf5;
    --stone: #cfc6cf;
    --address-band: #3a3238;
    --teal: #6fc2bd;
    --amber: #e8a23a;
    --rule: #6e6470;
  }
  * { box-sizing: border-box; margin: 0; padding: 0; }
  html, body { width: 927px; height: 1200px; overflow: hidden; background: var(--ink); }
  .flyer {
    position: relative; width: 927px; height: 1200px; overflow: hidden;
    font-family: Arial, Helvetica, sans-serif; color: var(--white);
  }
  .backdrop {
    position: absolute; inset: 0;
    background:
      radial-gradient(ellipse 60% 30% at 30% 12%, rgba(200,150,210,.45), transparent 70%),
      radial-gradient(ellipse 70% 25% at 75% 62%, rgba(180,110,200,.55), transparent 70%),
      linear-gradient(180deg, #3a1a3e 0%, #5a2a60 30%, #7a3e85 55%, #8c4c96 66%, #2a0f2c 76%, #0b0710 88%);
  }
  .crowd {
    position: absolute; left: 0; right: 0; top: 800px; height: 160px;
    background: linear-gradient(180deg, rgba(11,7,16,0) 0%, rgba(11,7,16,.85) 45%, var(--ink) 100%);
  }
  .event-series {
    position: absolute; top: 44px; left: 0; right: 0; text-align: center;
    font-family: "Michroma", sans-serif; font-size: 30px; letter-spacing: .55em;
    text-transform: uppercase;
  }
  .event-title {
    position: absolute; top: 118px; left: 0; right: 0; text-align: center;
    font-family: "Rubik Dirt", sans-serif; font-size: 132px; line-height: 1;
    letter-spacing: -.01em; font-weight: 400;
  }
  .event-acronym {
    position: absolute; left: 378px; top: 262px; width: 362px; height: 96px;
    background: var(--gold); transform: rotate(-8deg);
    font-family: "Rubik Dirt", sans-serif; font-size: 84px; line-height: 96px;
    text-align: center; color: var(--plum);
  }
  .photo-strip {
    position: absolute; left: 40px; top: 540px; width: 900px; height: 195px;
    display: flex; gap: 4px; transform: rotate(-5deg); transform-origin: left top;
  }
  .photo-strip .photo { flex: 1; border: 3px solid var(--white); }
  .photo--stage-blue { background: linear-gradient(160deg, #3a4fa0, #1b1f55); }
  .photo--band-mono { background: linear-gradient(160deg, #8a8a8a, #2a2a2a); }
  .photo--band-violet { background: linear-gradient(160deg, #7a4aa0, #2a1540); }
  .photo--artist { background: linear-gradient(160deg, #e6e6e6, #9a9a9a); }
  .date-band {
    position: absolute; left: 10px; top: 490px; width: 960px; height: 66px;
    background: var(--ink); transform: rotate(-8deg); transform-origin: left top;
    padding-left: 80px;
    font-family: "Oswald", sans-serif; font-weight: 700; font-size: 40px; line-height: 66px;
    text-transform: uppercase; white-space: nowrap;
  }
  .date-band .time { color: var(--cream-yellow); margin-left: 8px; }
  .venue-name {
    position: absolute; left: 505px; top: 700px; padding: 4px 16px;
    background: var(--ink); transform: rotate(-8deg); transform-origin: left top;
    font-family: "Oswald", sans-serif; font-weight: 600; font-size: 34px; line-height: 50px;
    color: var(--sky); text-transform: uppercase; white-space: nowrap;
  }
  .venue-address {
    position: absolute; left: 335px; top: 790px; padding: 2px 12px;
    background: var(--address-band); transform: rotate(-8deg); transform-origin: left top;
    font-family: "Oswald", sans-serif; font-weight: 600; font-size: 24px; line-height: 40px;
    color: var(--stone); text-transform: uppercase; white-space: nowrap;
  }
  .tagline {
    position: absolute; top: 960px; left: 0; right: 0; text-align: center;
    font-weight: 700; font-size: 19px; color: var(--teal);
  }
  .subline {
    position: absolute; top: 992px; left: 0; right: 0; text-align: center;
    font-style: italic; font-size: 13px;
  }
  .website {
    position: absolute; top: 1032px; left: 0; right: 0; text-align: center;
    font-size: 26px; color: var(--amber); letter-spacing: .02em;
  }
  .divider { position: absolute; top: 1083px; left: 25px; right: 25px; height: 1px; background: var(--rule); }
  .partner {
    position: absolute; top: 1100px; height: 72px; background: var(--white);
    display: flex; align-items: center; justify-content: center; gap: 6px;
    padding: 0 8px; text-align: center;
    font-size: 12px; font-weight: 700; color: var(--plum); line-height: 1.2;
  }
  .partner--charity { left: 27px; width: 136px; }
  .partner--venue { left: 178px; width: 127px; }
  .partner .mark { width: 14px; height: 14px; border-radius: 50%; background: var(--plum); flex: none; }
  .details {
    position: absolute; top: 1110px; left: 320px; right: 20px;
    font-size: 12.5px; line-height: 21px;
  }
  .details .label { color: var(--lilac); font-weight: 700; }
</style>
</head>
<body>
<main class="flyer">
  <div class="backdrop" role="img" aria-label="Worship crowd with raised hands under purple stage lights"></div>
  <div class="crowd" role="img" aria-label="Silhouette of a cheering concert crowd"></div>

  <p class="event-series">Hour of Glory</p>
  <h1 class="event-title">ENCOUNTER</h1>
  <p class="event-acronym">G.L.O.</p>

  <div class="photo-strip">
    <div class="photo photo--stage-blue" role="img" aria-label="Worship band on a blue-lit stage"></div>
    <div class="photo photo--band-mono" role="img" aria-label="Black and white photo of singers performing"></div>
    <div class="photo photo--band-violet" role="img" aria-label="Band with guitar under violet lights"></div>
    <div class="photo photo--artist" role="img" aria-label="Portrait of the debut artist"></div>
  </div>

  <p class="date-band">Wednesday, May 27th, 2015 <span class="time">7:00 PM to 8:15 PM</span></p>

  <p class="venue-name">The Harborview Chapel</p>
  <p class="venue-address">2715 W Maple Crest Rd, Fort Lauderdale, FL 33918</p>

  <p class="tagline">A Hour of Glory you will not want to miss! All ages welcome!</p>
  <p class="subline">Let's worship! Live band covering your favorite popular contemporary Christian music !</p>
  <p class="website">www.encounterpraiseGLO.example</p>

  <div class="divider"></div>

  <div class="partner partner--charity"><span class="mark"></span><span>The Open Hands Mission<br>Coral Bay County</span></div>
  <div class="partner partner--venue"><span>The Harborview Chapel</span></div>

  <div class="details">
    <p><span class="label">Event is FREE!!</span> Please bring a donation of gently used clothing items or new toiletry item.</p>
    <p><span class="label">Benefit for:</span> The Open Hands Mission. <span class="label">Brought to you by:</span> Delphine Marsh Music</p>
    <p><span class="label">This month's debut artist:</span> Talia Verhoeven - local Christian Singer / Songwriter.</p>
  </div>
</main>
</body>
</html>
```